need eczema bath soak label/bag

need you to recreate this please. ai file. recreate this exact image please. ...if you want a big tip, create some different styles.

Colors
0054AA
0677BA
7BADD7
CADEEF
E8F1F8

```html
<!DOCTYPE html>
<html lang="en">
<head>
<meta charset="utf-8">
<title>The Ocean Healed My A Bag – Bath Soak</title>
<link rel="stylesheet" href="https://fonts.googleapis.com/css2?family=Montserrat:wght@600;700;800&display=swap">
<style>
  :root {
    --ink: #0f3a40;
    --paper: #f3f4ef;
    --foam: #eef1ec;
    --sea-light: #7fd3c8;
    --sea: #3fb8ab;
    --shore: #e2dccb;
    --sand-light: #cfb88f;
    --sand: #b89a6a;
  }
  * { margin: 0; padding: 0; box-sizing: border-box; }
  html, body { width: 1198px; height: 1200px; overflow: hidden; background: var(--paper); }
  .label {
    position: relative;
    width: 1198px;
    height: 1200px;
    font-family: "Montserrat", sans-serif;
    color: var(--ink);
    text-align: center;
  }
  .beach-scene {
    position: absolute;
    inset: 0;
    background: linear-gradient(180deg,
      var(--paper) 0%,
      var(--foam) 24%,
      #dff0ec 29%,
      var(--sea-light) 36%,
      var(--sea) 42%,
      var(--sea-light) 48%,
      var(--foam) 53%,
      var(--shore) 58%,
      #e8e2d4 62%,
      var(--sand-light) 66%,
      var(--sand) 100%);
  }
  .title-block {
    position: absolute;
    left: 0; right: 0;
    top: 240px;
  }
  .title-the {
    font-size: 30px;
    font-weight: 800;
    letter-spacing: 0.28em;
    padding-left: 0.28em;
    line-height: 1;
  }
  .title-main {
    margin-top: 28px;
    font-size: 70px;
    font-weight: 700;
    line-height: 1.18;
  }
  .title-main .spaced { letter-spacing: 0.12em; padding-left: 0.12em; }
  .blurb {
    position: absolute;
    left: 0; right: 0;
    top: 590px;
    font-size: 13px;
    font-weight: 700;
    line-height: 1.9;
  }
  .tagline {
    position: absolute;
    left: 0; right: 0;
    top: 672px;
    font-size: 21px;
    font-weight: 700;
    letter-spacing: 0.06em;
    transform: translateX(-40px);
  }
  .brand {
    position: absolute;
    left: 0; right: 0;
    top: 890px;
    display: flex;
    justify-content: center;
    align-items: center;
    gap: 14px;
  }
  .brand-mark { width: 22px; height: 22px; background: var(--ink); }
  .brand-name { font-size: 22px; font-weight: 800; letter-spacing: 0.12em; }
</style>
</head>
<body>
<main class="label">
  <div class="beach-scene" role="img" aria-label="Photograph of a turquoise wave washing over a sandy beach, seen from above"></div>

  <header class="title-block">
    <p class="title-the">THE</p>
    <h1 class="title-main">
      <span class="spaced">OCEAN</span><br>
      HEALED<br>
      MY A BAG
    </h1>
  </header>

  <p class="blurb">
    Lorem ipsumLorem ipsumLorem<br>
    ipsumLorem ipsumLorem ipsumLorem<br>
    ipsumLorem ipsumLorem ipsum
  </p>

  <p class="tagline">OCEAN | IN A BA</p>

  <div class="brand">
    <span class="brand-mark"></span>
    <span class="brand-name">TIDEWELL</span>
  </div>
</main>
</body>
</html>
```